Medical Services company. Need a website that blows the competition out of the water

We need a web site designed to draw attention to our many services offered. We are a Medical Services business based out of Pennsylvania. We provide basic first aid staffing for events and businesses such as but not limited to: Fairs, Festivals, Carnivals, Sporting events, Large gatherings where a first aid station is needed, Concerts, Businesses with first aid needs . We provide training and certifications that are tailored to the customers needs. We provide Covid-19 pre screening and temperature monitoring. Our professionals consist of individuals with Basic First Aid, Certified Nursing Assistants, Medical Assistants, Emergency Medical Responders (EMR), Emergency Medical Technicians (EMT), and Nurses. I do not know how many pages I will need since we offer multiple different services. Our main services provided are: First Aid services, Covid-19 pre screen and temperatures, and Training/Certifications. You will have to use stock photos for now until I can get some actual photographs of our team.I have uploaded a copy of my brochure so you can get some information from there as well.

Target Market(s)

-For the first Aid and Covid-19 services: All Businesses, Sporting events, Event organizers
-Training: Everyone.

Font styles to use
Sans Serif

Requirements
Must have
• My colors are what is in the logos and Gray , need to have a way for customers to request a quote, design that grabs their attention. Should have pictures of medical providers attending to the sick or injured. Both in a office setting and in an emergency out in public. Should have pictures of an ambulance. Should also have pictures of staff taking temperatures and asking pre screening questions.
Nice to have
• I'll get back to you on that one

```html
<!DOCTYPE html>
<html lang="en">
<head>
<meta charset="utf-8">
<title>RMS Medical Services</title>
<link href="https://fonts.googleapis.com/css2?family=Poppins:wght@400;500;600;700&family=Oswald:wght@500;600&display=swap" rel="stylesheet">
<style>
  :root {
    --blue: #1c2fb0;
    --blue-deep: #14238a;
    --teal: #1bb8a5;
    --teal-dark: #12998a;
    --ink: #1d1f2b;
    --grey: #7b7f8c;
    --grey-light: #eef0f4;
    --white: #ffffff;
  }
  * { box-sizing: border-box; margin: 0; padding: 0; }
  html, body { width: 756px; height: 1200px; overflow: hidden; background: var(--white); }
  body { font-family: "Poppins", sans-serif; color: var(--ink); }
  .page { position: relative; width: 756px; height: 1200px; overflow: hidden; }

  /* Header */
  .site-header { position: absolute; top: 0; left: 0; width: 756px; height: 62px; display: flex; align-items: center; padding: 0 26px; background: var(--white); }
  .brand { display: flex; align-items: center; gap: 7px; white-space: nowrap; }
  .brand-dot { width: 14px; height: 14px; border-radius: 50%; background: var(--teal); flex: none; }
  .brand-name { font-weight: 700; font-size: 24px; color: var(--blue); line-height: 1; display: block; }
  .brand-sub { font-weight: 700; font-size: 7px; color: var(--blue); letter-spacing: .5px; display: block; margin-top: 2px; white-space: nowrap; }
  .main-nav { display: flex; gap: 20px; margin-left: auto; }
  .main-nav a { font-size: 8px; font-weight: 500; color: var(--grey); text-decoration: none; letter-spacing: .6px; text-transform: uppercase; white-space: nowrap; padding-bottom: 4px; }
  .main-nav a.is-active { color: var(--blue); border-bottom: 2px solid var(--blue); }
  .search-icon { margin-left: 18px; flex: none; }
  .emergency { display: flex; align-items: center; gap: 6px; margin-left: 16px; white-space: nowrap; }
  .emergency svg { flex: none; }
  .emergency-label { font-size: 7px; color: var(--grey); display: block; }
  .emergency-number { font-size: 15px; font-weight: 600; color: var(--teal); line-height: 1.1; display: block; white-space: nowrap; }

  /* Hero */
  .hero { position: absolute; top: 62px; left: 0; width: 756px; height: 420px; }
  .hero-photo { position: absolute; inset: 0; background: linear-gradient(160deg, #c9d2dc 0%, #8f9eb1 45%, #5d6d85 100%); }
  .hero-content { position: absolute; top: 120px; left: 0; width: 756px; text-align: center; color: var(--white); }
  .hero-title { font-family: "Oswald", sans-serif; font-weight: 600; font-size: 64px; color: var(--teal); letter-spacing: 3px; line-height: 1; }
  .hero-tagline { font-family: "Oswald", sans-serif; font-weight: 500; font-size: 20px; letter-spacing: 1px; margin-top: 14px; }
  .btn { display: inline-block; background: var(--teal); color: var(--white); font-size: 8px; font-weight: 600; letter-spacing: .6px; text-transform: uppercase; padding: 9px 20px; border-radius: 14px; text-decoration: none; white-space: nowrap; }
  .hero .btn { margin-top: 14px; }
  .slider-arrow { position: absolute; top: 244px; width: 22px; height: 22px; border-radius: 50%; background: rgba(255,255,255,.75); display: flex; align-items: center; justify-content: center; }
  .slider-arrow.prev { left: 24px; } .slider-arrow.next { right: 24px; }
  .hero-band { position: absolute; top: 430px; left: 0; }

  /* Welcome */
  .welcome { position: absolute; top: 520px; left: 0; width: 756px; text-align: center; }
  .section-title { font-size: 24px; font-weight: 700; color: var(--ink); }
  .welcome-text { width: 600px; margin: 12px auto 0; font-size: 8px; line-height: 1.6; color: var(--grey); }
  .welcome .btn { margin-top: 22px; }

  /* Safety band */
  .safety { position: absolute; top: 700px; left: 0; width: 756px; height: 245px; background: var(--blue); }
  .ambulance-art { position: absolute; top: 42px; left: 72px; width: 220px; height: 150px; border-radius: 6px; background: linear-gradient(180deg, #f4f6f9 0%, #d7dde5 100%); }
  .safety-copy { position: absolute; top: 52px; left: 380px; width: 330px; color: var(--white); }
  .safety-title { font-size: 22px; font-weight: 600; }
  .safety-copy p { font-size: 7.5px; line-height: 1.6; margin-top: 10px; opacity: .9; }

  /* Footer */
  .site-footer { position: absolute; top: 975px; left: 0; width: 756px; text-align: center; }
  .site-footer .brand { justify-content: center; }
  .site-footer .brand-name { font-size: 30px; }
  .footer-nav { display: flex; justify-content: center; gap: 20px; margin-top: 22px; }
  .footer-nav a { font-size: 8px; color: var(--grey); text-decoration: none; white-space: nowrap; }
  .social { display: flex; justify-content: center; gap: 10px; margin-top: 16px; }
  .social span { width: 20px; height: 20px; border-radius: 50%; background: var(--teal); }
  .copyright-bar { position: absolute; bottom: 0; left: 0; width: 756px; height: 28px; background: var(--teal); color: var(--white); font-size: 7px; display: flex; align-items: center; justify-content: center; }
</style>
</head>
<body>
<div class="page">

  <header class="site-header">
    <div class="brand">
      <span class="brand-dot"></span>
      <div><span class="brand-name">RMS</span><span class="brand-sub">Medical Services</span></div>
    </div>
    <nav class="main-nav">
      <a href="#" class="is-active">Home</a>
      <a href="#">About</a>
      <a href="#">Services</a>
      <a href="#">Request a Quote</a>
      <a href="#">Contact Us</a>
    </nav>
    <svg class="search-icon" width="11" height="11" viewBox="0 0 12 12"><circle cx="5" cy="5" r="3.8" fill="none" stroke="#1c2fb0" stroke-width="1.5"/><line x1="8" y1="8" x2="11" y2="11" stroke="#1c2fb0" stroke-width="1.5"/></svg>
    <div class="emergency">
      <svg width="20" height="20" viewBox="0 0 24 24"><path d="M6.6 10.8a15.1 15.1 0 0 0 6.6 6.6l2.2-2.2c.3-.3.7-.4 1-.2 1.1.4 2.3.6 3.6.6.6 0 1 .4 1 1V20c0 .6-.4 1-1 1A17 17 0 0 1 3 4c0-.6.4-1 1-1h3.5c.6 0 1 .4 1 1 0 1.3.2 2.5.6 3.6.1.3 0 .7-.2 1z" fill="#1c2fb0"/></svg>
      <div><span class="emergency-label">Emergency Call</span><span class="emergency-number">555-014-2290</span></div>
    </div>
  </header>

  <section class="hero">
    <div class="hero-photo" role="img" aria-label="Photo of paramedics giving first aid to an injured man lying on the ground"></div>
    <div class="hero-content">
      <div class="hero-title">RMS</div>
      <div class="hero-tagline">PROVIDING ALL OF YOUR HEALTH<br>AND SAFETY NEEDS</div>
      <a href="#" class="btn">Learn More</a>
    </div>
    <div class="slider-arrow prev"><svg width="8" height="8" viewBox="0 0 8 8"><path d="M5.5 1 2.5 4l3 3" fill="none" stroke="#555" stroke-width="1.4"/></svg></div>
    <div class="slider-arrow next"><svg width="8" height="8" viewBox="0 0 8 8"><path d="M2.5 1l3 3-3 3" fill="none" stroke="#555" stroke-width="1.4"/></svg></div>
  </section>

  <svg class="hero-band" width="756" height="80" viewBox="0 0 756 80">
    <path d="M0 10 Q378 60 756 10 V80 H0Z" fill="#1bb8a5"/>
    <path d="M0 40 Q378 62 756 40 V80 H0Z" fill="#ffffff"/>
    <circle cx="378" cy="34" r="18" fill="#1c2fb0" stroke="#ffffff" stroke-width="2"/>
  </svg>

  <section class="welcome">
    <h2 class="section-title">Welcome To RMS Medical Services</h2>
    <p class="welcome-text">We staff first aid stations for fairs, festivals, concerts, sporting events and workplaces across the region. Our team of first aid providers, nursing assistants, medical assistants, EMRs, EMTs and nurses is ready whenever you need care on site. We also offer tailored training and certification courses, plus pre-screening and temperature checks for staff and guests.</p>
    <a href="#" class="btn">View Services</a>
  </section>

  <section class="safety">
    <div class="ambulance-art" role="img" aria-label="Illustration of a white ambulance with red stripes"></div>
    <div class="safety-copy">
      <h2 class="safety-title">Keeping You Safe</h2>
      <p>Our responders arrive prepared, equipped and ready to act the moment help is needed at your event.</p>
      <p>By hiring trained health professionals, your staff and guests feel safer, work better and stay confident throughout the day.</p>
      <p>Our goal is to provide the best care and coverage to our customers and partners.</p>
      <p>We are proud to serve people and businesses throughout the state.</p>
    </div>
  </section>

  <footer class="site-footer">
    <div class="brand">
      <span class="brand-dot"></span>
      <div><span class="brand-name">RMS</span><span class="brand-sub">Medical Services</span></div>
    </div>
    <nav class="footer-nav">
      <a href="#">Home</a><a href="#">About</a><a href="#">Services</a><a href="#">Request a Quote</a><a href="#">Contact</a>
    </nav>
    <div class="social"><span></span><span></span><span></span></div>
  </footer>

  <div class="copyright-bar">Copyright © 2024 RMS Medical Services · All Rights Reserved</div>
</div>
</body>
</html>
```